Tidewell Giving Fund - New Website Designed

I need a site that looks like this http://www.ridgelanegiving.org for boat donations. So please replace the cars with boats.

```html
<!DOCTYPE html>
<html lang="en">
<head>
<meta charset="utf-8">
<title>Tidewell Giving Fund – Donate Your Boat</title>
<link rel="stylesheet" href="https://fonts.googleapis.com/css2?family=Roboto:wght@400;500;700;900&family=Open+Sans:wght@400;600;700&display=swap">
<style>
:root{
  --navy:#0f1f86;
  --navy-deep:#0a145e;
  --red:#d8161f;
  --white:#ffffff;
  --grey-band:#ebebeb;
  --text:#333333;
  --muted:#8a8a8a;
  --line:#cfcfcf;
  --dark-section:#2a201c;
}
*{box-sizing:border-box;margin:0;padding:0}
html,body{width:1200px;height:3000px;overflow:hidden}
body{position:relative;background:var(--white);font-family:"Open Sans",Arial,sans-serif;color:var(--text)}
.abs{position:absolute}

/* header */
.site-header{left:0;top:0;width:1200px;height:134px;background:linear-gradient(90deg,#1a2a8e 0%,#3b3f8f 35%,#7b2d45 70%,#1a2a8e 100%)}
.brand{left:146px;top:44px;display:flex;align-items:center;gap:14px}
.brand-dot{width:46px;height:46px;border-radius:50%;border:3px solid var(--white)}
.brand-name{font-family:"Roboto",Arial,sans-serif;font-weight:700;font-size:34px;color:var(--white)}
.call-box{left:692px;top:36px;width:380px;height:98px;background:var(--red);color:var(--white);display:flex;align-items:center;padding-left:50px;gap:16px}
.call-box .ring{width:56px;height:56px;border:3px solid var(--white);border-radius:50%;display:flex;align-items:center;justify-content:center}
.call-lines{font-family:"Roboto",Arial,sans-serif;line-height:1.1}
.call-title{font-size:19px;font-weight:500}
.call-number{font-size:30px;font-weight:700}
.call-note{font-size:11px;font-weight:500;margin-top:3px}

.main-nav{left:0;top:134px;width:1200px;height:76px;background:var(--navy)}
.main-nav ul{list-style:none;display:flex;gap:30px;position:absolute;left:196px;top:28px;font-family:"Roboto",Arial,sans-serif;font-weight:500;font-size:15px;color:var(--white)}
.main-nav .active{color:var(--red)}
.form-heading{left:692px;top:134px;width:380px;height:76px;background:var(--white);display:flex;align-items:center;justify-content:center;font-family:"Roboto",Arial,sans-serif;font-weight:700;font-size:22px;color:var(--navy-deep)}

/* hero */
.hero-photo{left:0;top:210px;width:1200px;height:556px;background:linear-gradient(100deg,#5b6470 0%,#c98a46 30%,#f2b45b 45%,#9a6a45 65%,#2f3a4c 100%)}
.donate-form{left:700px;top:210px;width:372px;height:556px;background:rgba(30,30,34,.82)}
.field{position:absolute;left:18px;width:328px;height:42px;background:var(--white);border-radius:2px;font-size:10px;color:#888;padding:14px 18px}
.field.half{width:158px}
.field.half::after{content:"";position:absolute;right:14px;top:18px;border:4px solid transparent;border-top-color:#999}
.donate-btn{position:absolute;left:18px;top:458px;width:328px;height:42px;background:var(--navy);color:var(--white);font-family:"Roboto",Arial,sans-serif;font-weight:700;font-size:15px;display:flex;align-items:center;justify-content:center}

/* benefits */
.benefit-band{left:0;top:766px;width:1200px;height:200px;background:var(--grey-band)}
.benefit-lead{left:0;top:750px;width:370px;height:216px;background:linear-gradient(120deg,#1b2680,#3c3f92 60%,#1b2680);clip-path:polygon(0 0,300px 0,370px 100%,0 100%)}
.benefit-lead .t1{position:absolute;left:30px;top:62px;font-family:"Roboto",Arial,sans-serif;font-size:29px;color:var(--white)}
.benefit-lead .t2{position:absolute;left:30px;top:90px;font-family:"Roboto",Arial,sans-serif;font-weight:900;font-size:50px;color:var(--red);letter-spacing:1px}
.benefit-lead .t3{position:absolute;left:94px;top:148px;font-family:"Roboto",Arial,sans-serif;font-weight:700;font-size:14px;color:var(--white)}
.benefit{position:absolute;top:808px;font-family:"Roboto",Arial,sans-serif;font-size:12px;font-weight:500;color:#222;line-height:1.35}
.benefit svg{display:block;margin:0 0 12px 0}

/* section titles */
.section-title{left:0;width:1200px;text-align:center;font-family:"Roboto",Arial,sans-serif;font-weight:700;font-size:30px;color:var(--red)}
.title-rule{height:1px;background:var(--line)}

/* how to donate */
.step{position:absolute;top:1150px;display:flex;align-items:center;gap:26px;font-family:"Roboto",Arial,sans-serif;font-weight:700;font-size:11px;color:#222;line-height:1.8}
.step-copy{position:absolute;top:1254px;width:300px;font-size:11px;line-height:1.8;color:var(--muted)}

/* why */
.why-section{left:0;top:1390px;width:1200px;height:620px;background:radial-gradient(ellipse at 70% 50%,#6b4a33 0%,#3a2a22 45%,#1c1614 100%)}
.why-title{top:1482px;color:var(--white)}
.why-rule{background:rgba(255,255,255,.7)}
.why-list{position:absolute;left:220px;top:1598px;list-style:none;font-size:15px;color:var(--white)}
.why-list li{display:flex;align-items:center;gap:16px;height:48px}
.why-list li::before{content:"";width:18px;height:18px;border-radius:50%;background:var(--red)}

/* faq */
.faq-photo{left:150px;top:2192px;width:446px;height:350px;background:linear-gradient(180deg,#8fb7d6 0%,#3f7fae 40%,#1d5c8e 100%)}
.faq-item{position:absolute;left:614px;width:444px;height:50px;border:1px solid #9a9a9a;border-radius:25px;font-size:15px;color:#222;padding:13px 22px}
.faq-item::after{content:"+";position:absolute;right:12px;top:14px;width:20px;height:20px;border-radius:50%;background:#666;color:var(--white);font-size:16px;line-height:19px;text-align:center}

/* footer */
.footer-tab{left:394px;top:2618px;width:414px;height:74px;background:var(--navy);border-radius:18px 18px 0 0;display:flex;align-items:center;justify-content:center;gap:12px}
.footer-tab .brand-dot{width:40px;height:40px}
.footer-tab .brand-name{font-size:28px}
.site-footer{left:0;top:2688px;width:1200px;height:312px;background:linear-gradient(180deg,#1a2a9a,#0f1c78)}
.foot-head{position:absolute;top:2784px;font-family:"Roboto",Arial,sans-serif;font-weight:700;font-size:12px;color:var(--white)}
.foot-text{position:absolute;top:2826px;font-size:12px;line-height:2.05;color:#e4e7ff}
.secure-badge{left:594px;top:2832px;width:104px;height:46px;background:var(--white);border-radius:4px}
.foot-call{left:740px;top:2778px;display:flex;align-items:center;gap:16px;color:var(--white)}
.foot-bottom{left:0;top:2946px;width:1200px;border-top:1px solid rgba(255,255,255,.3);text-align:center;font-size:12px;color:#e4e7ff;padding-top:18px}
</style>
</head>
<body>

<header class="site-header abs">
  <div class="brand abs"><span class="brand-dot"></span><span class="brand-name">Tidewell Giving Fund</span></div>
</header>
<div class="call-box abs">
  <span class="ring"><svg width="28" height="28" viewBox="0 0 24 24"><path d="M6.6 10.8a15 15 0 0 0 6.6 6.6l2.2-2.2c.3-.3.7-.4 1-.2 1.1.4 2.3.6 3.6.6.6 0 1 .4 1 1V20c0 .6-.4 1-1 1A17 17 0 0 1 3 4c0-.6.4-1 1-1h3.5c.6 0 1 .4 1 1 0 1.3.2 2.5.6 3.6.1.3 0 .7-.2 1z" fill="#fff"/></svg></span>
  <div class="call-lines"><div class="call-title">CALL TODAY TO DONATE</div><div class="call-number">1-800-555-0147</div><div class="call-note">Live Operates Available | 7 Days A Week</div></div>
</div>

<nav class="main-nav abs"><ul><li class="active">Why To Donate</li><li>How To Donate</li><li>FAQs</li><li>Contact Us</li></ul></nav>
<div class="form-heading abs">Donate Your Boat Online</div>

<div class="hero-photo abs" role="img" aria-label="Soldier in camouflage hugging a child at sunset beside a sailboat with a family on deck"></div>
<form class="donate-form abs">
  <div class="field" style="top:38px">Name</div>
  <div class="field" style="top:100px">Last Name</div>
  <div class="field" style="top:162px">Zip Code</div>
  <div class="field" style="top:222px">Phone Number</div>
  <div class="field" style="top:280px">E-Mail</div>
  <div class="field half" style="top:340px">Choose Year</div>
  <div class="field half" style="top:340px;left:188px">Choose Make Year</div>
  <div class="field" style="top:400px">Model Of Vehicle</div>
  <div class="donate-btn">DONATE NOW</div>
</form>

<div class="benefit-band abs"></div>
<div class="benefit-lead abs">
  <div class="t1">DONATE YOUR BOAT</div><div class="t2">VETERANS</div><div class="t3">MAKE A DIFFERENCE</div>
</div>
<div class="benefit" style="left:356px"><svg width="40" height="40" viewBox="0 0 40 40"><circle cx="20" cy="20" r="17" fill="none" stroke="#1a2a8e" stroke-width="2.5"/><text x="20" y="27" text-anchor="middle" font-size="20" font-weight="700" fill="#1a2a8e" font-family="Roboto,Arial,sans-serif">$</text></svg>You Have<br>No Cost</div>
<div class="benefit" style="left:494px"><svg width="48" height="40" viewBox="0 0 48 40"><rect x="2" y="12" width="26" height="16" fill="none" stroke="#222" stroke-width="2.5"/><path d="M28 16h10l6 7v5H28z" fill="none" stroke="#222" stroke-width="2.5"/><circle cx="11" cy="32" r="4" fill="#fff" stroke="#222" stroke-width="2.5"/><circle cx="36" cy="32" r="4" fill="#fff" stroke="#222" stroke-width="2.5"/></svg>Free Towing<br>Running or Not</div>
<div class="benefit" style="left:664px"><svg width="40" height="40" viewBox="0 0 40 40"><rect x="8" y="3" width="24" height="32" fill="none" stroke="#222" stroke-width="2.5"/><path d="M13 12h14M13 18h14M13 24h9" stroke="#222" stroke-width="2"/></svg>We Issue You<br>An IRS Tax Receipt</div>
<div class="benefit" style="left:834px"><svg width="44" height="40" viewBox="0 0 44 40"><rect x="3" y="6" width="36" height="26" fill="none" stroke="#222" stroke-width="2.5"/><circle cx="21" cy="19" r="6" fill="none" stroke="#222" stroke-width="2"/><path d="M9 12h6M27 26h6" stroke="#222" stroke-width="2"/></svg>We Take Care Of<br>All Paperwork</div>
<div class="benefit" style="left:994px"><svg width="40" height="40" viewBox="0 0 40 40"><rect x="6" y="4" width="22" height="30" fill="none" stroke="#222" stroke-width="2.5"/><path d="M34 6l-10 20" stroke="#222" stroke-width="3"/><path d="M11 13h12M11 19h8" stroke="#222" stroke-width="2"/></svg>We Take Care Of<br>DMV &amp; Smog Issues</div>

<h2 class="section-title abs" style="top:1016px">HOW TO DONATE</h2>
<div class="title-rule abs" style="left:316px;top:1036px;width:148px"></div>
<div class="title-rule abs" style="left:736px;top:1036px;width:148px"></div>

<div class="step" style="left:160px"><svg width="40" height="40" viewBox="0 0 24 24"><path d="M6.6 10.8a15 15 0 0 0 6.6 6.6l2.2-2.2c.3-.3.7-.4 1-.2 1.1.4 2.3.6 3.6.6.6 0 1 .4 1 1V20c0 .6-.4 1-1 1A17 17 0 0 1 3 4c0-.6.4-1 1-1h3.5c.6 0 1 .4 1 1 0 1.3.2 2.5.6 3.6.1.3 0 .7-.2 1z" fill="none" stroke="#d8161f" stroke-width="1.5"/></svg><span>CALL US AT 1-800-555-0147<br>FILL OUT THE ONLINE FORM</span></div>
<div class="step" style="left:454px"><svg width="58" height="40" viewBox="0 0 58 40"><rect x="2" y="10" width="30" height="18" fill="none" stroke="#222" stroke-width="2.5"/><path d="M32 14h12l8 8v6H32z" fill="none" stroke="#222" stroke-width="2.5"/><circle cx="12" cy="32" r="4" fill="#fff" stroke="#222" stroke-width="2.5"/><circle cx="44" cy="32" r="4" fill="#fff" stroke="#222" stroke-width="2.5"/></svg><span>WE TOW THE VEHICLE</span></div>
<div class="step" style="left:780px"><svg width="40" height="50" viewBox="0 0 40 50"><rect x="6" y="6" width="26" height="38" fill="none" stroke="#222" stroke-width="2.5"/><text x="19" y="32" text-anchor="middle" font-size="16" font-weight="700" fill="#222" font-family="Roboto,Arial,sans-serif">$</text></svg><span>TAX WRITE OFF</span></div>
<p class="step-copy" style="left:146px">At vero eos et accusamus et iusto odio dignissimos ducimus qui blanditiis praesentium voluptatum deleniti atque corrupti quos dolores et quas molestias</p>
<p class="step-copy" style="left:454px">At vero eos et accusamus et iusto odio dignissimos ducimus qui blanditiis praesentium voluptatum deleniti atque corrupti quos dolores et quas molestias</p>
<p class="step-copy" style="left:768px">At vero eos et accusamus et iusto odio dignissimos ducimus qui blanditiis praesentium voluptatum deleniti atque corrupti quos dolores et quas molestias</p>

<section class="why-section abs" role="img" aria-label="Silhouette of a saluting soldier against a waving flag at dusk"></section>
<h2 class="section-title why-title abs">WHY DONATE YOUR BOATS TO US</h2>
<div class="title-rule why-rule abs" style="left:164px;top:1500px;width:152px"></div>
<div class="title-rule why-rule abs" style="left:884px;top:1500px;width:152px"></div>
<ul class="why-list">
  <li>At vero eos et accusamus et iusto odio dignissimos ducimus qui blanditiis</li>
  <li>Praesentium voluptatum deleniti atque corrupti quos dolores et quas molestias</li>
  <li>Excepturi sint occaecati cupiditate non provident, similique sunt in culpa</li>
  <li>Qui officia deserunt mollitia animi, id est laborum et</li>
  <li>Dolorum fuga. Et harum quidem rerum facilis est et expedita distinctio.</li>
  <li>Nam libero tempore, cum soluta nobis est eligendi optio cumque nihil</li>
  <li>Impedit quo minus id quod maxime placeat facere possimus, omnis</li>
</ul>

<h2 class="section-title abs" style="top:2096px">FREQUENTLY ASKED QUESTIONS</h2>
<div class="title-rule abs" style="left:188px;top:2116px;width:152px"></div>
<div class="title-rule abs" style="left:860px;top:2116px;width:152px"></div>
<div class="faq-photo abs" role="img" aria-label="White motor yacht speeding across blue sea near a coastline"></div>
<div class="faq-item" style="top:2188px">Error sit voluptatem accusantium doloremque</div>
<div class="faq-item" style="top:2248px">Eaque ipsa quae ab illo inventore</div>
<div class="faq-item" style="top:2308px">Sunt explicabo. Nemo enim ipsam voluptatem</div>
<div class="faq-item" style="top:2368px">Sed quia consequuntur magni dolores</div>
<div class="faq-item" style="top:2428px">Sed quia consequuntur magni dolores</div>
<div class="faq-item" style="top:2488px">Sed quia consequuntur magni dolores</div>

<footer class="site-footer abs"></footer>
<div class="footer-tab abs"><span class="brand-dot"></span><span class="brand-name">Tidewell Giving Fund</span></div>
<div class="foot-head" style="left:144px">ABOUT TIDEWELL GIVING FUND</div>
<p class="foot-text" style="left:144px;width:230px">At vero eos et accusamus et iusto odio dignissimos ducimus qui blanditiis praesentium voluptatum deleniti atque corrupti quos dolores et quas</p>
<div class="foot-head" style="left:422px">NAVIGATION</div>
<p class="foot-text" style="left:422px">Why To Donate<br>How To Donate<br>FAQs<br>Contact Us</p>
<div class="foot-head" style="left:594px">SAFE &amp; SECURE</div>
<div class="secure-badge abs"></div>
<div class="foot-call abs">
  <span class="ring" style="width:52px;height:52px;border:3px solid #fff;border-radius:50%;display:flex;align-items:center;justify-content:center"><svg width="26" height="26" viewBox="0 0 24 24"><path d="M6.6 10.8a15 15 0 0 0 6.6 6.6l2.2-2.2c.3-.3.7-.4 1-.2 1.1.4 2.3.6 3.6.6.6 0 1 .4 1 1V20c0 .6-.4 1-1 1A17 17 0 0 1 3 4c0-.6.4-1 1-1h3.5c.6 0 1 .4 1 1 0 1.3.2 2.5.6 3.6.1.3 0 .7-.2 1z" fill="#fff"/></svg></span>
  <div class="call-lines"><div class="call-title">CALL TODAY TO DONATE</div><div class="call-number">1-800-555-0147</div><div class="call-note">Live Operates Available | 7 Days A Week</div></div>
</div>
<div class="foot-bottom abs">© 2017 Company Name | All Rights Reservd</div>

</body>
</html>
```